Word Page Templates x 5

1 x Letterhead Template with Header and Footer able to be printed to paper and pdf with non blurry resolution
- File attached looks ok on computer screen but does not print the same
- We are wanting it to print like it looks on the screen
- We are wanting it to print not fuzzy in resolution
- We are wanting the banner to be on the absolute edge of the page like it is on the computer screen
- We are needing to print this to paper and pdf with perfect resolution and colour

Please can someone help us!!

I have provided the logo files in our posession. If better resolutions are required please let us know.

We are also wanting 4 simple page templates to be setup in Landscape and Portrait orientation as well once we are happy with the letterhead that is provided samples have been provided
Updates

Hi all I have the vector files available now along with a Colour profile

Requirements
Must have
• Clear when printed on A4 Paper
Should not have
• Blurry images, Colour must be correct (same as Logo) - Please reference our website if need be ..... lomvira.com.au

```html
<!DOCTYPE html>
<html lang="en">
<head>
<meta charset="utf-8">
<title>Lomvira Letterhead</title>
<link rel="stylesheet" href="https://fonts.googleapis.com/css2?family=Source+Sans+3:wght@500;700&display=swap">
<style>
  :root {
    --navy: #233b7d;
    --green: #077a42;
    --paper: #ffffff;
  }
  * { margin: 0; padding: 0; box-sizing: border-box; }
  html, body { width: 849px; height: 1200px; overflow: hidden; background: var(--paper); }
  .letterhead { position: relative; width: 849px; height: 1200px; background: var(--paper); }
  .corner-accent {
    position: absolute; left: 0; top: 0; width: 62px; height: 211px;
    background: linear-gradient(160deg, var(--green), var(--navy));
  }
  .brand-name {
    position: absolute; left: 88px; top: 26px;
    font-family: "Source Sans 3", sans-serif; font-weight: 700;
    font-size: 68px; line-height: 1; letter-spacing: -0.5px; color: var(--navy);
  }
  .contact-list {
    position: absolute; left: 557px; top: 29px; list-style: none;
    font-family: "Source Sans 3", sans-serif; font-weight: 500;
    font-size: 14px; color: var(--navy);
  }
  .contact-item { display: flex; align-items: center; height: 23.5px; white-space: nowrap; }
  .contact-icon { width: 12px; height: 12px; margin-right: 15px; fill: var(--green); flex: none; }
  .footer-band {
    position: absolute; left: 0; top: 1171px; width: 849px; height: 11px;
    background: linear-gradient(90deg, var(--navy), var(--green));
  }
</style>
</head>
<body>
<main class="letterhead">
  <div class="corner-accent" role="img" aria-label="Decorative corner graphic in green and navy"></div>

  <div class="brand-name">LOMVIRA</div>

  <ul class="contact-list">
    <li class="contact-item">
      <svg class="contact-icon" viewBox="0 0 12 12"><path d="M6 0a4 4 0 0 0-4 4c0 3 4 8 4 8s4-5 4-8a4 4 0 0 0-4-4zm0 5.6A1.6 1.6 0 1 1 6 2.4a1.6 1.6 0 0 1 0 3.2z"/></svg>
      PO Box 2391, Marlow QLD 4230
    </li>
    <li class="contact-item">
      <svg class="contact-icon" viewBox="0 0 12 12"><path d="M2.4 0.5l2 2.2-1 1.4c.7 1.6 2 2.9 3.6 3.6l1.4-1 2.2 2-1.2 2.2C4.8 10.6 1.4 7.2.4 1.6z"/></svg>
      07 5500 1289
    </li>
    <li class="contact-item">
      <svg class="contact-icon" viewBox="0 0 12 12"><path d="M0 2h12v8H0zm1 1v.3l5 3.6 5-3.6V3zm0 1.6V9h3.4zM11 4.6L7.6 9H11z"/></svg>
      admin@lomvira.com.au
    </li>
    <li class="contact-item">
      <svg class="contact-icon" viewBox="0 0 12 12"><path d="M6 0a6 6 0 1 0 0 12A6 6 0 0 0 6 0zm0 1.2a4.8 4.8 0 0 1 4.8 4.8H7.2L4 2.4 2.3 3A4.8 4.8 0 0 1 6 1.2zM1.2 6l3 .8 2 3.9-.2.1A4.8 4.8 0 0 1 1.2 6zm6.2 4.5L6.2 7.2h4.5a4.8 4.8 0 0 1-3.3 3.3z"/></svg>
      www.lomvira.com.au
    </li>
  </ul>

  <div class="footer-band" role="img" aria-label="Decorative footer band in navy fading to green"></div>
</main>
</body>
</html>
```